Report Cover and Format For Company

Hello, I would like a report cover for my company and document format that will be used for reports, proposals and documents to customers.

Industry/Entity Type

Information Technology

```html
<!DOCTYPE html>
<html lang="en">
<head>
<meta charset="utf-8">
<title>Ondravel Technology Solutions – Report Folder</title>
<link rel="stylesheet" href="https://fonts.googleapis.com/css2?family=Questrial&display=swap">
<style>
  :root {
    --page-bg: #e4e4e4;
    --brand-blue: #1384c9;
    --brand-blue-deep: #0f74b6;
    --brand-cyan: #12cfe9;
    --panel-grey-light: #f3f3f3;
    --panel-grey-dark: #dcdcdc;
    --white: #ffffff;
  }
  * { margin: 0; padding: 0; box-sizing: border-box; }
  html, body {
    width: 1200px;
    height: 1029px;
    overflow: hidden;
    background: var(--page-bg);
    font-family: "Questrial", sans-serif;
  }
  .folder {
    position: absolute;
    left: 194px;
    top: 216px;
    width: 800px;
    height: 572px;
    display: flex;
    gap: 3px;
  }
  .panel {
    position: relative;
    width: 398px;
    height: 572px;
    overflow: hidden;
  }
  .back-cover { background: var(--brand-blue); }
  .front-cover {
    background: linear-gradient(90deg, var(--brand-blue-deep) 0%, var(--brand-blue) 100%);
  }

  /* Back cover */
  .back-brand {
    position: absolute;
    left: 150px;
    top: 270px;
    color: var(--white);
  }
  .back-brand .brand-row {
    display: flex;
    align-items: center;
    gap: 8px;
    font-size: 30px;
    letter-spacing: 1px;
    line-height: 1;
  }
  .back-brand .brand-square {
    width: 13px;
    height: 13px;
    background: var(--white);
  }
  .back-brand .brand-sub {
    margin-top: 10px;
    font-size: 14px;
    line-height: 1.05;
  }
  .back-footer {
    position: absolute;
    left: 30px;
    right: 30px;
    top: 528px;
    display: flex;
    align-items: center;
    gap: 6px;
    color: var(--white);
    font-size: 7px;
  }
  .back-footer .rule {
    flex: 1;
    height: 1px;
    background: rgba(255,255,255,0.75);
  }

  /* Front cover */
  .cover-title {
    position: absolute;
    top: 52px;
    left: 28px;
    color: var(--white);
    font-size: 27px;
    font-weight: 400;
    letter-spacing: 0;
    line-height: 1;
    white-space: nowrap;
  }
  .cover-shapes {
    position: absolute;
    left: 0;
    top: 0;
    width: 398px;
    height: 572px;
  }
  .front-brand {
    position: absolute;
    left: 18px;
    top: 482px;
    color: var(--brand-blue);
  }
  .front-brand .brand-row {
    display: flex;
    align-items: center;
    gap: 7px;
    font-size: 24px;
    line-height: 1;
    letter-spacing: 1px;
  }
  .front-brand .brand-square {
    width: 11px;
    height: 11px;
    background: var(--brand-blue);
  }
  .front-brand .brand-sub {
    margin-top: 8px;
    font-size: 15px;
    line-height: 1.05;
  }
  .contact-block {
    position: absolute;
    right: 22px;
    top: 431px;
    text-align: right;
    color: var(--white);
    font-style: normal;
    font-size: 6.5px;
    line-height: 11px;
  }
  .social-links {
    position: absolute;
    right: 22px;
    top: 472px;
    display: flex;
    gap: 10px;
  }
  .social-links span {
    width: 18px;
    height: 18px;
    background: var(--white);
    border-radius: 2px;
  }
</style>
</head>
<body>
  <main class="folder">
    <section class="panel back-cover">
      <div class="back-brand">
        <div class="brand-row"><span class="brand-square"></span>ONDRAVEL</div>
        <div class="brand-sub">TECHNOLOGY<br>SOLUTIONS</div>
      </div>
      <div class="back-footer">
        <span class="rule"></span>
        <span class="web">www.ondraveltech.com</span>
        <span class="rule"></span>
      </div>
    </section>

    <section class="panel front-cover">
      <h1 class="cover-title">TECHNOLOGY SOLUTIONS</h1>
      <svg class="cover-shapes" viewBox="0 0 398 572" aria-hidden="true">
        <defs>
          <linearGradient id="greyWedge" x1="0" y1="0" x2="1" y2="0">
            <stop offset="0" stop-color="#f3f3f3"/>
            <stop offset="1" stop-color="#dcdcdc"/>
          </linearGradient>
        </defs>
        <polygon points="0,224 0,572 301,572" fill="url(#greyWedge)"/>
        <polygon points="398,488 301,572 398,572" fill="#12cfe9"/>
      </svg>
      <div class="front-brand">
        <div class="brand-row"><span class="brand-square"></span>ONDRAVEL</div>
        <div class="brand-sub">TECHNOLOGY<br>SOLUTIONS</div>
      </div>
      <address class="contact-block">
        P: 555 014 2290 &nbsp; E: hello@ondraveltech.com<br>
        www.ondraveltech.com<br>
        48 Harbor Lane, Suite 2, Fairview 5521
      </address>
      <div class="social-links" aria-label="Social links">
        <span></span><span></span><span></span>
      </div>
    </section>
  </main>
</body>
</html>
```